Vitoplume.com

I need a web design for a Online Wellness Center based in Chicago, IL and it's called "Vitoplume" We provide Health risk assessment to individuals and interventions. Our portal has a Health Activity tracker where our members record health activities and aerobic miles and biometric data. Our Online wellness center tracks the participant's progress toward health goals and awards points for completed activities.
I started working on this website but the designer was not able to designer a website which describes what we do. I need a fresh look on this project. I need a very attractive, responsive website which says what we do.
These are the things we do.
1. We provide Health Risk Assessments to individuals and Co-operations
2. We Provide Free health screenings to undeserved communities
3. Assist individuals access free or affordable medications
4. We ask providers/doctors to see (or do a complete physical) one individual free of charge once a year (those individuals who are no insured and don't have money to pay from their pocket)
5. Assist patient access lab work at low cost
Our goal is to provide services that will lower the cost of care for our members.

Here is the website: www.vitoplume.com still underdevelopment. PLEASE DO NOT COPY THIS STYLE OF WEBSITE. IT'S A BAD DESIGN AND THAT IS WHY I'M RE-DESIGNING THE SITE

Target Market(s)

Health individuals between the age of 21 to 65 Plus years old. Insured and uninsured

Industry/Entity Type

Health And Wellness

Coding

Coded - Design and coding required

Number of Pages Required

5+ page

Colors
0292cd

Requirements
Must have
• I'm still working on this websiteHere is the menu: Home, About us, Services, Health Screening, Providers, Contacts
• Please see. www.vitoplume.com
Nice to have
• Event calender
• Upcoming Event
• Medication
• Lab assist
• Providers/Free Clinics

```html
<!DOCTYPE html>
<html lang="en">
<head>
<meta charset="utf-8">
<title>Vitoplume – Online Wellness Center</title>
<link href="https://fonts.googleapis.com/css2?family=Oswald:wght@500;700&family=Open+Sans:wght@400;600;700&display=swap" rel="stylesheet">
<style>
:root{
  --blue:#0292cd;
  --navy:#17337a;
  --deep:#0e2a66;
  --green:#8cc63f;
  --green-dark:#6fa62b;
  --ink:#444a55;
  --muted:#7a808a;
  --light:#f1f3f6;
  --line:#dde2e8;
  --white:#fff;
}
*{margin:0;padding:0;box-sizing:border-box}
html,body{width:1200px;height:2776px;overflow:hidden}
body{font-family:"Open Sans",Arial,sans-serif;color:var(--ink);background:var(--white);font-size:13px;line-height:1.55}
.site{position:relative;width:1200px;height:2776px}
.h-title{font-family:"Oswald",Arial,sans-serif;color:var(--navy);text-transform:uppercase;text-align:center;font-weight:500;font-size:28px;letter-spacing:.5px}
.btn{display:inline-block;background:var(--navy);color:var(--white);font-size:11px;font-weight:700;text-transform:uppercase;padding:7px 16px;border-radius:3px;letter-spacing:.5px}
.btn-round{border-radius:14px;background:#2f3d56;font-size:10px;padding:5px 14px}

/* header */
.header{height:112px;display:flex;align-items:center;justify-content:space-between;padding:0 68px;background:var(--white)}
.brand{display:flex;align-items:center;gap:10px;font-family:"Open Sans",Arial,sans-serif;font-weight:700;font-size:30px;color:var(--blue)}
.brand-dot{width:34px;height:34px;border-radius:50%;background:var(--green)}
.header-right{display:flex;flex-direction:column;align-items:flex-end;gap:10px}
.call{display:flex;align-items:center;gap:8px;font-size:12px;color:var(--navy);font-weight:600;line-height:1.2}
.call small{display:block;font-weight:400;color:var(--muted);font-size:10px}
.nav{display:flex;gap:4px}
.nav a{font-size:11px;font-weight:700;color:var(--navy);text-transform:uppercase;padding:7px 13px;text-decoration:none}
.nav a.active{background:var(--green);color:var(--white)}

/* hero */
.hero{position:relative;height:678px;overflow:hidden}
.hero-photo{position:absolute;inset:0;background:linear-gradient(100deg,#eef3f8 0%,#dfe7ef 45%,#c9d6e3 70%,#aebfcf 100%)}
.hero-figure{position:absolute;right:120px;bottom:0;width:420px;height:640px;background:linear-gradient(180deg,#e9eef2 0%,#f8f9fb 60%,#dce4ec 100%);border-radius:200px 200px 0 0;opacity:.9}
.hero-copy{position:absolute;left:68px;top:120px;width:560px}
.hero-copy h1{font-family:"Oswald",Arial,sans-serif;font-weight:700;font-size:64px;line-height:1.02;color:var(--deep);text-transform:uppercase}
.hero-copy h2{font-family:"Oswald",Arial,sans-serif;font-weight:500;font-size:24px;color:var(--white);background:var(--blue);display:inline-block;padding:4px 14px;margin:26px 0 18px;text-transform:uppercase}
.hero-copy p{font-size:14px;color:var(--deep);font-style:italic;width:470px;margin-bottom:26px}

/* about */
.about{height:410px;padding-top:36px;text-align:center}
.about .lead{width:1000px;margin:14px auto 28px;font-size:11px;color:var(--muted);line-height:1.6}
.features{display:flex;justify-content:center;gap:40px}
.feature{width:230px}
.feature .icon{width:92px;height:92px;border-radius:50%;margin:0 auto 12px;display:flex;align-items:center;justify-content:center}
.feature h3{font-family:"Oswald",Arial,sans-serif;font-weight:500;color:var(--navy);font-size:18px;text-transform:uppercase}
.feature p{font-size:10.5px;color:var(--muted);margin:4px 0 10px;line-height:1.45}

/* benefits */
.benefits{position:relative;height:400px;background:var(--light);overflow:hidden}
.benefits-photo{position:absolute;right:0;top:0;width:600px;height:400px;background:linear-gradient(90deg,var(--light) 0%,#e4ebf2 30%,#d2dde8 100%)}
.benefits-copy{position:absolute;left:68px;top:42px;width:500px}
.benefits-copy .h-title{text-align:left;font-size:28px}
.benefits-copy .intro{font-size:11px;color:var(--blue);font-weight:600;text-transform:uppercase;margin:12px 0 14px;line-height:1.5}
.ticks{list-style:none;margin-bottom:16px}
.ticks li{display:flex;align-items:center;gap:8px;font-size:12.5px;color:var(--navy);line-height:1.85}

/* overview */
.overview{height:528px;padding-top:34px;text-align:center}
.overview .sub{font-size:13px;color:var(--muted);margin:8px 0 14px}
.tabs{display:flex;margin:0 68px;border-bottom:2px solid var(--green)}
.tabs span{font-size:11.5px;color:var(--navy);padding:6px 14px}
.tabs span.on{background:var(--green);color:var(--white);font-weight:600}
.tab-body{display:flex;gap:36px;margin:22px 68px 0;text-align:left}
.tab-photo{width:440px;height:330px;background:linear-gradient(135deg,#3f6b8e 0%,#6f98b7 50%,#b9cfdf 100%)}
.tab-text{flex:1}
.tab-text h3{font-family:"Oswald",Arial,sans-serif;color:var(--blue);font-weight:500;font-size:22px;text-transform:uppercase}
.tab-text h4{font-size:13px;color:var(--navy);text-transform:uppercase;font-weight:700;margin:10px 0 4px}
.tab-text p{font-size:11px;color:var(--muted)}
.bullets{display:grid;grid-template-columns:1fr 1fr;gap:2px 20px;list-style:none;margin-top:12px}
.bullets li{font-size:11px;color:var(--ink);display:flex;gap:6px;align-items:center}
.bullets li::before{content:"";width:6px;height:6px;background:var(--green);border-radius:50%}

/* cta */
.cta{height:160px;background:var(--blue);display:flex;align-items:center;padding:0 150px;gap:20px}
.cta-text{flex:1;color:var(--white)}
.cta-text h3{font-family:"Oswald",Arial,sans-serif;font-weight:500;font-size:30px}
.cta-text p{font-size:12px;text-transform:uppercase;letter-spacing:.6px;opacity:.9}
.cta-btn{background:var(--green);color:var(--white);font-size:15px;font-weight:600;padding:14px 30px;border-radius:4px;border:2px solid var(--white)}

/* events */
.events{height:368px;padding-top:28px;text-align:center}
.events .lead{width:1060px;margin:10px auto 18px;font-size:10.5px;color:var(--muted);line-height:1.5}
.cards{display:flex;gap:20px;margin:0 72px}
.card{flex:1;text-align:left;background:var(--white);border:1px solid var(--line)}
.card-photo{position:relative;height:120px;background:linear-gradient(135deg,#5b86b0,#a8c3d8)}
.card:nth-child(2) .card-photo{background:linear-gradient(135deg,#6c9c5a,#c2d9a9)}
.card:nth-child(3) .card-photo{background:linear-gradient(135deg,#3d6f96,#9fc2dc)}
.card:nth-child(4) .card-photo{background:linear-gradient(135deg,#7c5b86,#c7b3d0)}
.date{position:absolute;left:0;bottom:0;background:var(--green);color:var(--white);font-size:10px;font-weight:700;padding:3px 8px;line-height:1.2;text-align:center}
.card-body{padding:8px 10px 10px}
.card-body h4{font-size:12px;color:var(--navy);font-weight:700}
.card-body p{font-size:10px;color:var(--muted);line-height:1.4;margin:3px 0 5px}
.author{font-size:10px;color:var(--blue);display:flex;gap:5px;align-items:center}

/* footer */
.footer{position:absolute;left:0;right:0;bottom:0;height:116px;background:var(--deep);color:#c9d3e6}
.foot-nav{display:flex;justify-content:center;gap:22px;font-size:11px;padding-top:16px}
.foot-nav a{color:#c9d3e6;text-decoration:none}
.foot-nav a:first-child{color:var(--white);font-weight:600}
.foot-row{display:flex;align-items:center;justify-content:space-between;padding:12px 68px 0}
.email{width:200px;height:28px;border:1px solid #4b6396;border-radius:3px;font-size:10px;padding:6px 8px;color:#8d9dbb}
.foot-brand{display:flex;align-items:center;gap:8px;font-weight:700;font-size:20px;color:var(--white)}
.foot-brand i{width:20px;height:20px;border-radius:50%;background:var(--green)}
.socials{display:flex;gap:8px;width:200px;justify-content:flex-end}
.socials i{width:24px;height:24px;border-radius:50%;background:#2e4b85}
.copy{text-align:center;font-size:10px;color:#8d9dbb;margin-top:8px}
</style>
</head>
<body>
<div class="site">

<header class="header">
  <div class="brand"><span class="brand-dot"></span>Vitoplume</div>
  <div class="header-right">
    <div class="call">
      <svg width="22" height="22" viewBox="0 0 24 24"><circle cx="12" cy="12" r="12" fill="#0292cd"/><path d="M8 6.5l2 0 1 3-1.5 1a7 7 0 0 0 4 4l1-1.5 3 1v2c0 .8-.7 1.5-1.5 1.5A10 10 0 0 1 6.5 8c0-.8.7-1.5 1.5-1.5z" fill="#fff"/></svg>
      <div><small>Call Us</small>123-456-7890</div>
    </div>
    <nav class="nav">
      <a class="active" href="#">Home</a><a href="#">About Us</a><a href="#">Services</a><a href="#">Health Screening</a><a href="#">Providers</a><a href="#">Contacts</a>
    </nav>
  </div>
</header>

<section class="hero">
  <div class="hero-photo" role="img" aria-label="Bright clinic interior background"></div>
  <div class="hero-figure" role="img" aria-label="Smiling doctor in white coat with stethoscope"></div>
  <div class="hero-copy">
    <h1>Did you how about<br>your risk factor</h1>
    <h2>We avails health screening services</h2>
    <p>9 out of 10 adults carry hidden risk factors. Regular screening helps find them early, so small lifestyle changes can protect your health for years.</p>
    <span class="btn">Read More</span>
  </div>
</section>

<section class="about">
  <h2 class="h-title">About Us</h2>
  <p class="lead">Vitoplume is an online wellness center helping individuals and companies understand their health through risk assessments, free screenings and simple interventions. Members record activities, aerobic miles and biometric data, watch their progress toward goals and earn points for every completed step. We connect people with affordable medication, low cost lab work and providers who see one uninsured patient free each year, so that the cost of care stays lower for everyone we serve.</p>
  <div class="features">
    <div class="feature">
      <div class="icon" style="background:var(--blue)"><svg width="44" height="44" viewBox="0 0 44 44"><rect x="8" y="16" width="28" height="12" rx="6" fill="#fff"/><rect x="22" y="16" width="14" height="12" rx="6" fill="#8cc63f"/></svg></div>
      <h3>Medication</h3>
      <p>Help finding free or affordable medicines through trusted assistance programs.</p>
      <span class="btn btn-round">Read More</span>
    </div>
    <div class="feature">
      <div class="icon" style="background:var(--green)"><svg width="44" height="44" viewBox="0 0 44 44"><circle cx="22" cy="15" r="7" fill="#fff"/><path d="M9 36c0-8 6-12 13-12s13 4 13 12z" fill="#fff"/></svg></div>
      <h3>Providers</h3>
      <p>Doctors who offer one complete yearly physical free to an uninsured person.</p>
      <span class="btn btn-round">Read More</span>
    </div>
    <div class="feature">
      <div class="icon" style="background:var(--navy)"><svg width="44" height="44" viewBox="0 0 44 44"><path d="M17 8h10v4h-2v9l8 14H11l8-14v-9h-2z" fill="#fff"/><path d="M14 30h16l3 5H11z" fill="#8cc63f"/></svg></div>
      <h3>Lab Test</h3>
      <p>Access to needed lab work at a low cost through our partner laboratories.</p>
      <span class="btn btn-round">Read More</span>
    </div>
    <div class="feature">
      <div class="icon" style="background:var(--blue)"><svg width="44" height="44" viewBox="0 0 44 44"><rect x="10" y="12" width="24" height="22" fill="#fff"/><rect x="19" y="16" width="6" height="14" fill="#0292cd"/><rect x="15" y="20" width="14" height="6" fill="#0292cd"/></svg></div>
      <h3>Free Clinics</h3>
      <p>Free health screenings held in underserved communities around the city.</p>
      <span class="btn btn-round">Read More</span>
    </div>
  </div>
</section>

<section class="benefits">
  <div class="benefits-photo" role="img" aria-label="Group of smiling doctors and nurses"></div>
  <div class="benefits-copy">
    <h2 class="h-title">Benefits of our wellness services</h2>
    <p class="intro">Our community is working toward a healthier future, join the wellness services and choose the suitable plans for you.</p>
    <ul class="ticks">
      <li><svg width="14" height="14" viewBox="0 0 14 14"><path d="M2 7l3 3 7-7" stroke="#8cc63f" stroke-width="2.4" fill="none"/></svg>Free wellness Articles</li>
      <li><svg width="14" height="14" viewBox="0 0 14 14"><path d="M2 7l3 3 7-7" stroke="#8cc63f" stroke-width="2.4" fill="none"/></svg>Health Tips &amp; keep your health record</li>
      <li><svg width="14" height="14" viewBox="0 0 14 14"><path d="M2 7l3 3 7-7" stroke="#8cc63f" stroke-width="2.4" fill="none"/></svg>Free health assessment report</li>
      <li><svg width="14" height="14" viewBox="0 0 14 14"><path d="M2 7l3 3 7-7" stroke="#8cc63f" stroke-width="2.4" fill="none"/></svg>Affordable Screening</li>
      <li><svg width="14" height="14" viewBox="0 0 14 14"><path d="M2 7l3 3 7-7" stroke="#8cc63f" stroke-width="2.4" fill="none"/></svg>Accurate Report card</li>
      <li><svg width="14" height="14" viewBox="0 0 14 14"><path d="M2 7l3 3 7-7" stroke="#8cc63f" stroke-width="2.4" fill="none"/></svg>Health screening camps</li>
      <li><svg width="14" height="14" viewBox="0 0 14 14"><path d="M2 7l3 3 7-7" stroke="#8cc63f" stroke-width="2.4" fill="none"/></svg>Saving your time, money</li>
    </ul>
    <span class="btn">Read More</span>
  </div>
</section>

<section class="overview">
  <h2 class="h-title">An over view of our wellness solutions</h2>
  <p class="sub">Our wellness Features - Measurable Results at an Affordable Price</p>
  <div class="tabs"><span class="on">Health Tools</span><span>Wellness Store</span><span>Announcements</span><span>Patient Communications</span><span>Health News</span><span>To do List</span><span>Healthy Living Guidelines</span></div>
  <div class="tab-body">
    <div class="tab-photo" role="img" aria-label="Medical team working in an operating room"></div>
    <div class="tab-text">
      <h3>We provides wellness tools</h3>
      <h4>Health Activity Tracker</h4>
      <p>Our tracker lets members log daily activities, aerobic miles and biometric data in one place. Progress toward each health goal is shown clearly, and points are awarded for every completed activity to keep you motivated.</p>
      <h4>Online Intervention</h4>
      <p>Personal online programs guide members after their risk assessment, with simple steps, reminders and coaching that fit into a busy day and lead to lasting change.</p>
      <ul class="bullets">
        <li>Weight care plan for healthy eating</li>
        <li>Quit smoking plan with coaching</li>
        <li>Resilience plan for stress relief</li>
        <li>Daily exercise plan for fitness</li>
        <li>Alcohol care plan for balance</li>
      </ul>
    </div>
  </div>
</section>

<section class="cta">
  <svg width="56" height="56" viewBox="0 0 56 56"><rect x="8" y="12" width="40" height="36" rx="3" fill="none" stroke="#fff" stroke-width="3"/><path d="M8 22h40M18 6v10M38 6v10" stroke="#fff" stroke-width="3"/><path d="M20 34l6 6 11-12" stroke="#8cc63f" stroke-width="3.5" fill="none"/></svg>
  <div class="cta-text">
    <h3>Need a Doctor for Check-up?</h3>
    <p>Just make an appointment &amp; you're done!</p>
  </div>
  <span class="cta-btn">Get an Appointment</span>
</section>

<section class="events">
  <h2 class="h-title">Our Upcoming Events</h2>
  <p class="lead">Join us at free screening days, wellness walks and health talks across Chicago. Our events bring care closer to the community and help every member stay on track with their goals, meet local providers and learn simple habits for a healthier life with family and friends.</p>
  <div class="cards">
    <article class="card">
      <div class="card-photo" role="img" aria-label="Community health screening event"><span class="date">12<br>JUN</span></div>
      <div class="card-body"><h4>LOREM IPSUM DOLAR SIT</h4><p>Free blood pressure and sugar checks for local families this weekend.</p><span class="author">● Mara Quell</span></div>
    </article>
    <article class="card">
      <div class="card-photo" role="img" aria-label="Outdoor wellness walk"><span class="date">18<br>JUN</span></div>
      <div class="card-body"><h4>LOREM IPSUM DOLAR SIT</h4><p>A morning wellness walk with points awarded for every mile completed.</p><span class="author">● Mara Quell</span></div>
    </article>
    <article class="card">
      <div class="card-photo" role="img" aria-label="Doctor giving a health talk"><span class="date">24<br>JUN</span></div>
      <div class="card-body"><h4>LOREM IPSUM DOLAR SIT</h4><p>Meet providers and learn how to reduce your personal health risks.</p><span class="author">● Mara Quell</span></div>
    </article>
    <article class="card">
      <div class="card-photo" role="img" aria-label="Low cost lab testing day"><span class="date">30<br>JUN</span></div>
      <div class="card-body"><h4>LOREM IPSUM DOLAR SIT</h4><p>Low cost lab work day with fast results sent to your member page.</p><span class="author">● Mara Quell</span></div>
    </article>
  </div>
</section>

<footer class="footer">
  <nav class="foot-nav"><a href="#">Home</a><a href="#">About Us</a><a href="#">Services</a><a href="#">Health Screening</a><a href="#">Providers</a><a href="#">Contacts</a></nav>
  <div class="foot-row">
    <div class="email">Email Address</div>
    <div class="foot-brand"><i></i>Vitoplume</div>
    <div class="socials"><i></i><i></i><i></i><i></i></div>
  </div>
  <p class="copy">© 2015 Vitoplume. Privacy Policy | Terms of Use</p>
</footer>

</div>
</body>
</html>
```